OSKA Dispatch (e-update) Design

Using Constant Contact, we need a template news email designed that we can re-use on a regular basis. Our news email would feature an average of 10 content blocks and would love the chance to feature photos with at least 8 of the content blocks. Whatever is designed would need to be transferrable to our constant contact account. Our news content per news item is short, usually a paragraph with links back to our site and events. The template would need a banner that really showcases the email design or helps brand the email. We are looking for a design that is sophisticated but youthful. We recently rebranded our firm and are great with the use of our new corporate colors.

Target Market(s)

Our association members of 700 professional real estate managers of highrises and buildings.

Colors

Designer to choose colors to be used in the design.

Requirements
Must have
• Email template design in Constant Contact to include a banner, area for 8 to 10 content blocks with cooresponding photos. A sophisticated and colorful design that makes people want to read the content.
Should not have
• Clip art

```html
<!DOCTYPE html>
<html lang="en">
<head>
<meta charset="utf-8">
<title>OSKA Dispatch</title>
<link href="https://fonts.googleapis.com/css2?family=Arimo:wght@400;700&display=swap" rel="stylesheet">
<style>
:root{
  --page:#f1f1f1;
  --header:#f6f6f6;
  --card:#ffffff;
  --navy:#4b5993;
  --ink:#2b2b2b;
  --muted:#666666;
  --button:#5e74bd;
  --rule:#6d6d6d;
  --pink:#c2317a;
  --blue:#4d5d99;
  --sun:#f7c21c;
  --sky:#8fb7e6;
  --magenta:#e0348f;
}
*{box-sizing:border-box;margin:0;padding:0}
html,body{width:1200px;height:3742px;overflow:hidden}
body{background:var(--page);font-family:"Arimo",Arial,sans-serif;color:var(--ink);position:relative}

.masthead{position:absolute;left:0;top:0;width:1200px;height:180px;background:var(--header)}
.brand{position:absolute;left:80px;top:34px;display:flex;align-items:center;gap:22px}
.brand-square{width:96px;height:96px;background:var(--navy)}
.brand-name{font-size:104px;font-weight:700;color:var(--navy);letter-spacing:2px;line-height:1}
.contact{position:absolute;right:76px;top:30px;list-style:none;text-align:right}
.contact li{font-size:25px;color:var(--muted);height:42px;display:flex;justify-content:flex-end;align-items:center;gap:12px}
.contact svg{width:26px;height:26px}

.hero{position:absolute;left:0;top:180px;width:1200px;height:586px;
  background:linear-gradient(115deg,var(--sun) 0%,#f5d640 28%,var(--sky) 48%,#a9c6ee 62%,#7f8fe0 78%,var(--magenta) 100%)}

.issue{position:absolute;left:80px;top:846px;width:1040px;display:grid;grid-template-columns:481px 481px;column-gap:78px;row-gap:40px}
.story{height:479px;background:var(--card);box-shadow:0 8px 22px rgba(0,0,0,.14);text-align:center;position:relative}
.story-photo{height:200px;width:100%}
.photo-desk{background:linear-gradient(90deg,#cfcfcf 0%,#d9d6d2 12%,#8a8580 16%,#b7b0a8 45%,#6e5e52 70%,#3d3530 84%,#c9c6c3 88%,#e2e2e2 100%)}
.photo-network{background:linear-gradient(90deg,#d6d8de 0%,#c4c9d3 20%,#a8afbd 55%,#cdd2dc 80%,#e9eaee 100%)}
.photo-ballot{background:linear-gradient(90deg,#2c2a33 0%,#5a4c48 18%,#c9c4c4 45%,#2a6fc2 70%,#1e8fe0 90%,#3a9be8 100%)}
.photo-office{background:linear-gradient(90deg,#4a4a4a 0%,#6a625c 14%,#2d2a2a 35%,#8b8580 60%,#d7d7d7 82%,#bdbdbd 100%)}
.photo-keyboard{background:linear-gradient(90deg,#c8c8cc 0%,#a4b2c4 18%,#7f90a8 50%,#9aa8bb 80%,#d8d8dc 100%)}
.photo-signing{background:linear-gradient(90deg,#3a2f2a 0%,#5b4638 20%,#2b2420 45%,#8a7a6e 70%,#b8b0a8 88%,#dcdcdc 100%)}
.story-title{margin-top:46px;font-size:27px;font-weight:700;color:var(--navy);line-height:1.27;padding:0 30px;height:69px;overflow:hidden}
.story-date{margin-top:8px;font-size:25px;color:var(--ink)}
.read-more{position:absolute;left:147px;top:382px;width:187px;height:56px;background:var(--button);border-radius:5px;color:#fff;font-size:19px;font-weight:700;display:flex;align-items:center;justify-content:center;gap:10px;text-decoration:none}
.read-more svg{width:34px;height:14px}

.footer{position:absolute;left:0;top:3500px;width:1200px;text-align:center}
.footer-rule{width:1040px;height:5px;background:var(--rule);margin:0 auto}
.footer-brand{margin-top:28px;display:inline-flex;align-items:center;gap:14px}
.footer-brand .brand-square{width:62px;height:62px}
.footer-brand .brand-name{font-size:66px}
.copyright{margin-top:30px;font-size:25px;color:var(--muted)}
</style>
</head>
<body>
<header class="masthead">
  <div class="brand"><span class="brand-square"></span><span class="brand-name">OSKA</span></div>
  <ul class="contact">
    <li>(800) 555-0142
      <svg viewBox="0 0 24 24"><path fill="var(--pink)" d="M6.6 10.8c1.4 2.8 3.8 5.1 6.6 6.6l2.2-2.2c.3-.3.7-.4 1-.2 1.1.4 2.3.6 3.6.6.6 0 1 .4 1 1V20c0 .6-.4 1-1 1C10.6 21 3 13.4 3 4c0-.6.4-1 1-1h3.5c.6 0 1 .4 1 1 0 1.3.2 2.5.6 3.6.1.3 0 .7-.2 1z"/></svg></li>
    <li>(800) 555-0187
      <svg viewBox="0 0 24 24"><path fill="var(--blue)" d="M6 3h12v5H6zM4 9h16a2 2 0 0 1 2 2v6h-4v4H6v-4H2v-6a2 2 0 0 1 2-2zm4 7v3h8v-3z"/></svg></li>
    <li>hello@oska-members.org
      <svg viewBox="0 0 24 24"><path fill="var(--blue)" d="M2 5h20v14H2zm2 2v.5l8 5 8-5V7l-8 5z"/></svg></li>
  </ul>
</header>

<div class="hero" role="img" aria-label="Group of smiling colleagues looking down at the camera, overlaid with yellow, blue and pink colour bands"></div>

<main class="issue">
  <article class="story">
    <div class="story-photo photo-desk" role="img" aria-label="Hands holding a phone beside a laptop"></div>
    <h2 class="story-title">Value Analysis of Income Real Estate - VAL310</h2>
    <p class="story-date">Next Offering: 11/9/2018</p>
    <a class="read-more" href="#">Read More <svg viewBox="0 0 34 14"><path d="M0 7h31M25 1l6 6-6 6" stroke="#fff" stroke-width="2" fill="none"/></svg></a>
  </article>
  <article class="story">
    <div class="story-photo photo-desk" role="img" aria-label="Hands holding a phone beside a laptop"></div>
    <h2 class="story-title">Planning, Cash Flow, and Statements for Income...</h2>
    <p class="story-date">Next Offering: 11/13/2018</p>
    <a class="read-more" href="#">Read More <svg viewBox="0 0 34 14"><path d="M0 7h31M25 1l6 6-6 6" stroke="#fff" stroke-width="2" fill="none"/></svg></a>
  </article>
  <article class="story">
    <div class="story-photo photo-network" role="img" aria-label="Hand touching a network of connected people icons"></div>
    <h2 class="story-title">Building a Strong Property Operations Team - LDR204</h2>
    <p class="story-date">Next Offering: 11/13/2018</p>
    <a class="read-more" href="#">Read More <svg viewBox="0 0 34 14"><path d="M0 7h31M25 1l6 6-6 6" stroke="#fff" stroke-width="2" fill="none"/></svg></a>
  </article>
  <article class="story">
    <div class="story-photo photo-ballot" role="img" aria-label="Voter marking a ballot at a flag-draped booth"></div>
    <h2 class="story-title">What the Midterm Election Results May Mean to the...</h2>
    <p class="story-date">Webinar Date: 11/13/2018</p>
    <a class="read-more" href="#">Read More <svg viewBox="0 0 34 14"><path d="M0 7h31M25 1l6 6-6 6" stroke="#fff" stroke-width="2" fill="none"/></svg></a>
  </article>
  <article class="story">
    <div class="story-photo photo-office" role="img" aria-label="Professional reviewing papers at an office desk"></div>
    <h2 class="story-title">CAM, Tax, and Insurance Recoveries for the Property...</h2>
    <p class="story-date">Webinar Date: 11/14/2018</p>
    <a class="read-more" href="#">Read More <svg viewBox="0 0 34 14"><path d="M0 7h31M25 1l6 6-6 6" stroke="#fff" stroke-width="2" fill="none"/></svg></a>
  </article>
  <article class="story">
    <div class="story-photo photo-keyboard" role="img" aria-label="Hands typing on a laptop keyboard"></div>
    <h2 class="story-title">Using Spreadsheets to Sharpen Your Property Management...</h2>
    <p class="story-date">Webinar Date: 12/5/2018</p>
    <a class="read-more" href="#">Read More <svg viewBox="0 0 34 14"><path d="M0 7h31M25 1l6 6-6 6" stroke="#fff" stroke-width="2" fill="none"/></svg></a>
  </article>
  <article class="story">
    <div class="story-photo photo-desk" role="img" aria-label="Hands holding a phone beside a laptop"></div>
    <h2 class="story-title">Value Analysis of Income Real Estate - VAL310</h2>
    <p class="story-date">Next Offering: 11/9/2018</p>
    <a class="read-more" href="#">Read More <svg viewBox="0 0 34 14"><path d="M0 7h31M25 1l6 6-6 6" stroke="#fff" stroke-width="2" fill="none"/></svg></a>
  </article>
  <article class="story">
    <div class="story-photo photo-signing" role="img" aria-label="Hand signing a document with a pen"></div>
    <h2 class="story-title">What the Midterm Election Results May Mean to the...</h2>
    <p class="story-date">Webinar Date: 11/13/2018</p>
    <a class="read-more" href="#">Read More <svg viewBox="0 0 34 14"><path d="M0 7h31M25 1l6 6-6 6" stroke="#fff" stroke-width="2" fill="none"/></svg></a>
  </article>
  <article class="story">
    <div class="story-photo photo-network" role="img" aria-label="Hand touching a network of connected people icons"></div>
    <h2 class="story-title">Building a Strong Property Operations Team - LDR204</h2>
    <p class="story-date">Next Offering: 11/13/2018</p>
    <a class="read-more" href="#">Read More <svg viewBox="0 0 34 14"><path d="M0 7h31M25 1l6 6-6 6" stroke="#fff" stroke-width="2" fill="none"/></svg></a>
  </article>
  <article class="story">
    <div class="story-photo photo-desk" role="img" aria-label="Hands holding a phone beside a laptop"></div>
    <h2 class="story-title">Planning, Cash Flow, and Statements for Income...</h2>
    <p class="story-date">Next Offering: 11/13/2018</p>
    <a class="read-more" href="#">Read More <svg viewBox="0 0 34 14"><path d="M0 7h31M25 1l6 6-6 6" stroke="#fff" stroke-width="2" fill="none"/></svg></a>
  </article>
</main>

<footer class="footer">
  <div class="footer-rule"></div>
  <div class="footer-brand"><span class="brand-square"></span><span class="brand-name">OSKA</span></div>
  <p class="copyright">©Organization of Skilled Asset Managers. All Rights Reserved.</p>
</footer>
</body>
</html>
```